International Internship Provider Needs Catalogue Layout & Design

We need a catalogue/booklet created to send out to university students and study abroad offices. We provide international internships to university students and young professionals in a range of fields in nine cities across the globe. Our program includes guaranteed internship, accommodation, social events, and support from staff. We would like to provide a clean, glossy, and picture-heavy publication to promote our program and website. We'd like to use captivating colors and the final product should convey what our program does and express the fun of living abroad with the professionalism of an internship.

Reason: We've increased the budget by $100, and we understand the project is a large undertaking. Thank you!

We would like each location to be two pages with large images of that location as well as all of the copy in the word document attached. Attached on the images is as an example of another catalogue we liked the style of for you to look at it. If you need any more details or would like me to break up the copy into sections please do not hesitate to ask. thank you!  

I've added new file of content that includes everything in the previous file plus more information, but on separate pages to help make it clear what information goes together. The location should still be a two-page spread that includes a large location image. We would like to have a quote from a student on each of those pages as well. 

I've added more photos for the location pages labeled by the location (ex: London_girls). I've also added some photos for Project Kelvo and new content. Please contact me with any questions. 

Reason: We realized we've asked for a few more edits from designers and we appreciate the time it takes to be make these constant edits. Thank you!

University students and recent college graduates. Usually the target market is between 21-23 years of age, and most students who travel abroad are female.

University

• It must be at least 10 pages and use the logo I've attached. Please be sure to look at the word document that is full of content that will be used in the project. Large photos of the locations are ideal as well 2 pages for each location.
• I have loads of photos I can give to you to use in the document, but you can use placeholders for now or some of the photos I've attached. I've also included a document full of copy that will need to be in the document just to give you an idea of where things will be displayed.

```html
<!DOCTYPE html>
<html lang="en">
<head>
<meta charset="utf-8">
<title>Program Catalogue Spread – Support &amp; Staff</title>
<link rel="stylesheet" href="https://fonts.googleapis.com/css2?family=Roboto:wght@300;400&display=swap">
<style>
  :root {
    --backdrop: #000000;
    --page-blue: #4f83b5;
    --panel-blue: #b3dcf3;
    --spine-blue: #3a6797;
    --accent-lime: #c3dc1f;
    --ink: #22457c;
    --photo-top: #c9c3b9;
    --photo-mid: #6f6660;
    --photo-low: #8a8f98;
  }
  * { margin: 0; padding: 0; box-sizing: border-box; }
  html, body {
    width: 1200px; height: 923px; overflow: hidden;
    background: var(--backdrop);
  }
  .spread {
    position: relative; width: 1200px; height: 923px;
    font-family: "Roboto", "Helvetica Neue", Arial, sans-serif;
    color: var(--ink);
  }
  .page-left {
    position: absolute; left: 46px; top: 90px; width: 381px; height: 741px;
    background: var(--page-blue);
  }
  .page-right {
    position: absolute; left: 459px; top: 90px; width: 694px; height: 741px;
    background: var(--page-blue);
  }
  .spine { position: absolute; left: 0; top: 0; width: 1200px; height: 923px; pointer-events: none; }
  .feature-box {
    position: absolute; left: 99px; top: 174px; width: 325px; height: 552px;
    background: var(--panel-blue);
    padding: 34px 50px 0 38px;
  }
  .group-photo {
    position: absolute; left: 459px; top: 90px; width: 694px; height: 324px;
    background: linear-gradient(180deg, var(--photo-top) 0%, var(--photo-top) 10%, var(--photo-mid) 40%, var(--photo-low) 100%);
  }
  .info-panel {
    position: absolute; left: 459px; top: 414px; width: 694px; height: 312px;
    background: var(--panel-blue);
    padding: 42px 125px 0 18px;
  }
  h2 {
    font-weight: 300; font-size: 28px; line-height: 29px; letter-spacing: -0.2px;
    color: var(--ink);
  }
  p {
    font-weight: 300; font-size: 12.2px; line-height: 15.6px;
    color: var(--ink);
  }
  .feature-box section + section { margin-top: 26px; }
  .info-panel section + section { margin-top: 30px; }
</style>
</head>
<body>
<div class="spread">
  <div class="page-left"></div>
  <div class="page-right"></div>

  <div class="feature-box">
    <section>
      <h2>Individual Support:</h2>
      <p>Starting from the first phone call, we work with you one-on-one to learn about your personal interests and career objectives. Our Program Advisors will provide visa support, pre-departure information, and answer any questions through phone calls and a series of webinars.&nbsp; Once in your new home, our Location Coordinators will have an orientation for you and will be available to you 24/7 as an emergency contact.</p>
    </section>
    <section>
      <h2>Unique Social Events &amp; Excursions</h2>
      <p>An internship is hard work, but we have planned several city-specific events and excursions to help you foster new relationships with other interns and enjoy all that you host city has to offer.&nbsp; We give you the insiders guide to your new city since all our local staff are locals they give you the best mix of must dos and one of a kind experiences. Social events may range from trekking through the Blue Mountains in Sydney, dinning on homemade pasta in Florence, or pouring the perfect pint in Dublin.</p>
    </section>
  </div>

  <div class="group-photo" role="img" aria-label="Group photo of program participants standing together outdoors in front of a building sign"></div>

  <div class="info-panel">
    <section>
      <h2>Local Staff:</h2>
      <p>In each of our nine locations, we have local staff that is there to ensure that all aspects of the program are fulfilled for each participant. Our Location Coordinators live in that city year-round and can provide you with a real insider’s advice about local customs, the language, places to see, and where to shop. Our Location Coordinators are in daily communication with our home office in Millbrook, VA so you know all our staff is updated on your internship and time abroad.</p>
    </section>
    <section>
      <h2>University Partnerships:</h2>
      <p>Our collaborative and successful university custom partnerships have also allowed students to fulfill their academic and career goals as part of an affordable experience that meets the needs of all stakeholders. Custom academic internships are currently available in all locations and our university partners include some of the top US universities.</p>
    </section>
  </div>

  <svg class="spine" viewBox="0 0 1200 923" aria-hidden="true">
    <polygon points="396,90 427,90 427,130" fill="var(--accent-lime)"/>
    <rect x="423" y="90" width="5" height="666" fill="var(--accent-lime)"/>
    <rect x="427" y="90" width="32" height="741" fill="var(--spine-blue)"/>
    <polygon points="427,793 427,831 401,831" fill="var(--spine-blue)"/>
  </svg>
</div>
</body>
</html>
```